LA's Newest HEMP Facial Oil and Body Oil Packaging Project

We need a packaging concept for a Hemp based facial oil and body oil. We need label design for the bottle and carton graphics. I am attaching a few reference photos. The target demographic is women between 17-35 year old. Products need to be able to stand out in crowded stores with clear calls to action.
1oz Dropper Bottle with Unit Carton - Hemp Facial Oil
4oz PET Bottle with Unit Carton - Hemp + Rose Facial Oil

```html
<!DOCTYPE html>
<html lang="en">
<head>
<meta charset="utf-8">
<title>Verdant Skincare – Hemp Facial Oil Packaging</title>
<link rel="stylesheet" href="https://fonts.googleapis.com/css2?family=Montserrat:wght@300;400;600;800&family=Josefin+Sans:wght@300;400;600&family=Lato:wght@300;400;700;900&display=swap">
<style>
  :root{
    --bg:#c9ccd1;
    --panel:#e6e8ec;
    --green:#4e8a2e;
    --green-dark:#3d7022;
    --leaf-light:#8cc152;
    --ink:#111111;
    --grey-text:#3b3b3b;
    --silver-a:#9a9a9a;
    --silver-b:#e2e2e2;
    --white:#ffffff;
  }
  *{box-sizing:border-box;margin:0;padding:0}
  html,body{width:1200px;height:1200px;overflow:hidden}
  body{background:var(--bg);position:relative;font-family:"Lato",sans-serif}

  .carton{position:absolute;left:60px;top:100px;height:1000px;display:flex;box-shadow:0 10px 30px rgba(0,0,0,.15)}
  .carton-side{width:170px;height:100%;background:linear-gradient(180deg,var(--green),var(--green-dark));position:relative}
  .side-emblem{position:absolute;left:50%;top:60px;transform:translateX(-50%);width:84px;height:84px;border:3px solid var(--white);border-radius:50%}
  .side-title{position:absolute;left:50%;top:600px;transform:translate(-50%,-50%) rotate(90deg);white-space:nowrap;
    font-family:"Montserrat",sans-serif;font-weight:800;font-size:58px;color:var(--white);letter-spacing:1px}

  .carton-front{width:420px;height:100%;background:var(--panel);position:relative}
  .brand-rule{position:absolute;top:60px;left:40px;right:40px;height:1px;background:var(--grey-text)}
  .brand-mark{position:absolute;top:51px;left:50%;transform:translateX(-50%);width:18px;height:18px;background:var(--panel);border:2px solid var(--grey-text)}
  .brand-name{position:absolute;top:100px;width:100%;text-align:center;font-family:"Josefin Sans",sans-serif;font-weight:400;font-size:22px;letter-spacing:4px;color:var(--grey-text)}
  .front-hemp{position:absolute;top:165px;width:100%;text-align:center;font-family:"Montserrat",sans-serif;font-weight:800;font-size:108px;line-height:1;color:var(--ink);letter-spacing:-2px}
  .front-sub{position:absolute;top:285px;left:58px;font-family:"Josefin Sans",sans-serif;font-weight:300;font-size:34px;color:var(--green)}
  .front-leaf{position:absolute;top:340px;left:20px;width:390px;height:460px;
    background:radial-gradient(closest-side,var(--leaf-light),var(--green) 60%,rgba(78,138,46,0) 100%)}

  .band-green{position:absolute;left:0;right:0;background:var(--green);color:var(--white);text-align:center;font-family:"Josefin Sans",sans-serif;letter-spacing:3px}
  .band-green b{font-weight:600}
  .band-silver{position:absolute;left:0;right:0;background:linear-gradient(90deg,var(--silver-a),var(--silver-b) 50%,var(--silver-a));text-align:center;color:var(--ink)}
  .band-silver .small{font-family:"Lato",sans-serif;font-weight:400;letter-spacing:-.5px}
  .band-silver .big{font-family:"Lato",sans-serif;font-weight:900;letter-spacing:-1px}
  .volume{position:absolute;left:0;right:0;text-align:center;font-family:"Lato",sans-serif;font-weight:300;color:var(--ink)}

  .carton-front .band-green{top:800px;height:50px;line-height:52px;font-size:17px}
  .carton-front .band-silver{top:850px;height:90px;padding-top:14px}
  .carton-front .small{font-size:17px}
  .carton-front .big{font-size:36px;line-height:1.1}
  .carton-front .volume{top:960px;font-size:20px}

  .label{position:absolute;left:710px;top:330px;width:430px;height:560px;background:var(--panel);box-shadow:0 10px 30px rgba(0,0,0,.15);overflow:hidden}
  .label .brand-rule{top:30px;left:30px;right:30px}
  .label .brand-mark{top:23px;width:14px;height:14px}
  .label .brand-name{top:58px;font-size:16px;letter-spacing:3px}
  .label-hemp{position:absolute;left:72px;top:226px;transform:translate(-50%,-50%) rotate(-90deg);white-space:nowrap;
    font-family:"Montserrat",sans-serif;font-weight:800;font-size:86px;line-height:1;color:var(--ink);letter-spacing:-2px}
  .label-sub{position:absolute;left:30px;top:374px;font-family:"Josefin Sans",sans-serif;font-weight:300;font-size:16px;color:var(--green)}
  .label-leaf{position:absolute;left:135px;top:85px;width:290px;height:320px;
    background:radial-gradient(closest-side,var(--leaf-light),var(--green) 60%,rgba(78,138,46,0) 100%)}
  .label .band-green{top:405px;height:42px;line-height:44px;font-size:15px}
  .label .band-silver{top:447px;height:78px;padding-top:12px}
  .label .small{font-size:14px}
  .label .big{font-size:29px;line-height:1.1}
  .label .volume{top:530px;left:24px;text-align:left;font-size:13px}
</style>
</head>
<body>
  <section class="carton">
    <div class="carton-side">
      <div class="side-emblem"></div>
      <div class="side-title">HEMP FACIAL OIL</div>
    </div>
    <div class="carton-front">
      <div class="brand-rule"></div>
      <div class="brand-mark"></div>
      <div class="brand-name">VERDANT SKINCARE</div>
      <h1 class="front-hemp">HEMP</h1>
      <div class="front-sub">FACIAL OIL</div>
      <div class="front-leaf" role="img" aria-label="Illustration of a green hemp leaf"></div>
      <div class="band-green">BRIGHTEN AND <b>HYDRATE</b></div>
      <div class="band-silver">
        <div class="small">WITH HEMP OIL</div>
        <div class="big">ALL SKIN TYPES</div>
      </div>
      <div class="volume">1 fl Oz.30ml</div>
    </div>
  </section>

  <section class="label">
    <div class="brand-rule"></div>
    <div class="brand-mark"></div>
    <div class="brand-name">VERDANT SKINCARE</div>
    <div class="label-leaf" role="img" aria-label="Illustration of a green hemp leaf"></div>
    <div class="label-hemp">HEMP</div>
    <div class="label-sub">FACIAL OIL</div>
    <div class="band-green">BRIGHTEN AND HYDRATE</div>
    <div class="band-silver">
      <div class="small">WITH HEMP OIL</div>
      <div class="big">ALL SKIN TYPES</div>
    </div>
    <div class="volume">1 fl Oz.30ml</div>
  </section>
</body>
</html>
```